Family History Site Home Page Redesign

KinTrail (http://www.kintrail-example.net) is a new genealogy website. We would like a fresh home page. We provide innovative tools for the serious genealogist in a Chatterbox-like environment. The tagline is “Easy to research. Easy to share.” The page must convey both the research and sharing aspects of the product and benefits such as:
• Modern
• Intuitive
• Easy
• Free
• Fast (Save 90% data entry time)
• Integrate with LineageHub
• Control your tree; nobody can edit without your permission
Our target audience is women age 30-60. Please examine our current home page at KinTrail-example.net. You will be creating a revised homepage that appeals to this demographic. Feel free to use any part of the existing page. You may use any of the materials provided, but you are not required to use everything.
You may use other images as long as you have the copyright or it is public domain. For instance, you could show an image of a woman, teenager, or young adult enjoying an glimphone or tablet, a civil war soldier, a wagon train, etc.
Please stay with the Layered Canvas style (Use Roboto font and other guidelines from https://layeredcanvas-example.io/guides/layered-canvas/overview.html) and our color palette (brand guidelines included).
We would like the following elements:
• Header (must keep login link in upper right corner)
• Primary call to action (Currently “Get started”)
• Section about “Easy to Research” with link to read more
• Section about “Easy to Share” with link to read more
• Section about LineageHub integration with link to read more
Optional:
• Marlene's Story (video)
• Links to demo trees and pages for Walter Pembrook and/or Henry Castwell
• Pricing section – please include and do not change
• Footer with the same links it now has.

The homepage must be responsive so it can be viewed on mobile phones and tablets.

Here are some examples of homepages we like:
https://www.brightquill-example.com/orbit/
https://www.heritagevault-example.com/dna/
https://www.panelprobe-example.com/
https://snapalbums-example.com/
https://www.zoomride-example.com/
http://www.lineagehub-example.org

Target Market(s)

women 30-60

Number of Pages Required

1 page

Font styles to use
Sans Serif

Requirements
Must have
• Sections for "Easy to Research," "Easy to Share," and "LineageHub Integration," with "learn more" links.
• Pricing section.
• Our basic plan is free forever.
Nice to have
• Happy family or happy person with a computer. Most of the homepages we have liked concentrated on people's faces. Please find public domain pictures or have copyright to pictures.
• What is KinTrail section.
• Section for 1-3 sample videos. KinTrail makes slideshow videos from family photos.Please make sure it is obvious that these are sample videos.
• Place for Marlene's video and/or the walk through.

```html
<!DOCTYPE html>
<html lang="en">
<head>
<meta charset="utf-8">
<title>KinTrail — Easy to Research, Easy to Share</title>
<link rel="stylesheet" href="https://fonts.googleapis.com/css2?family=Lato:wght@400;700;900&display=swap">
<style>
:root{
  --green:#6cbf3e;
  --blue:#4a88c7;
  --slate:#3e5468;
  --ink:#3b3b3b;
  --muted:#777;
  --faint:#b5b5b5;
  --sky:#e9f3fb;
  --sand:#f7f0c8;
  --white:#fff;
  --line:#e2e2e2;
}
*{box-sizing:border-box;margin:0;padding:0}
html,body{width:1200px;height:3742px;overflow:hidden}
body{position:relative;font-family:"Lato",Arial,sans-serif;color:var(--ink);background:var(--white)}
.abs{position:absolute}
.brand{font-weight:900;font-size:34px;color:var(--white);letter-spacing:.5px;white-space:nowrap}
.btn{position:absolute;display:flex;align-items:center;justify-content:center;font-weight:700;font-size:15px;text-transform:uppercase;letter-spacing:.5px;text-decoration:none;border-radius:3px;white-space:nowrap}
.btn-green{background:var(--green);color:var(--white)}
.btn-outline{border:2px solid #cfcfcf;color:var(--muted);text-transform:none;font-weight:400;font-size:14px;background:var(--white)}
.section-title{position:absolute;font-weight:900;font-size:26px;text-transform:uppercase;letter-spacing:.5px;line-height:1.3;white-space:nowrap}
.checks{position:absolute;list-style:none;font-size:13px;line-height:1.6}
.checks li{position:relative;padding-left:32px;margin-bottom:6px}
.checks li::before{content:"";position:absolute;left:0;top:4px;width:12px;height:12px;border:1.5px solid currentColor;border-radius:2px}
.checks li::after{content:"";position:absolute;left:3px;top:6px;width:6px;height:3px;border-left:2px solid currentColor;border-bottom:2px solid currentColor;transform:rotate(-45deg)}
.art{position:absolute;border-radius:6px}
.hero{left:0;top:0;width:1200px;height:559px;background:linear-gradient(160deg,#4b4a47 0%,#2f2e2c 45%,#3f3b36 100%)}
.share{left:0;top:1000px;width:1200px;height:430px;background:var(--blue)}
.video{left:0;top:1859px;width:1200px;height:441px;background:linear-gradient(120deg,#56623f,#7b8a55 50%,#4e5a37)}
.demo{left:0;top:2300px;width:1200px;height:445px;background:var(--sky)}
.plan{position:absolute;top:2847px;width:320px;height:559px;background:var(--white);border:1px solid var(--line);box-shadow:0 2px 6px rgba(0,0,0,.08);text-align:center}
.plan-featured{background:var(--blue);border-color:var(--blue);top:2838px;height:578px;color:var(--white)}
.plan-name{margin-top:42px;font-weight:900;font-size:22px;text-transform:uppercase}
.plan-rule{width:260px;height:1px;background:var(--line);margin:20px auto 0}
.plan-featured .plan-rule{background:rgba(255,255,255,.4)}
.plan-price{margin-top:22px;font-size:31px;font-weight:400}
.plan-features{list-style:none;text-align:left;margin:40px 0 0 28px;font-size:13px;line-height:1}
.plan-features li{position:relative;padding-left:24px;margin-bottom:19px}
.plan-features li::before{content:"";position:absolute;left:2px;top:0;width:8px;height:4px;border-left:2px solid currentColor;border-bottom:2px solid currentColor;transform:rotate(-45deg)}
.plan-features li.off{color:var(--faint)}
.plan-featured .plan-features li.off{color:rgba(255,255,255,.5)}
.plan-btn{position:absolute;left:28px;bottom:40px;width:264px;height:46px;background:var(--slate);color:var(--white);display:flex;align-items:center;justify-content:center;font-size:13px;font-weight:700;text-transform:uppercase;border-radius:2px}
.plan-featured .plan-btn{background:var(--green)}
.footer{left:0;top:3523px;width:1200px;height:219px;background:var(--blue);border-top:8px solid var(--green);color:var(--white)}
.foot-head{position:absolute;font-weight:900;font-size:15px;text-transform:uppercase;letter-spacing:.5px}
.foot-links{position:absolute;list-style:none;font-size:13px;line-height:1.65}
.social{position:absolute;display:flex;gap:20px}
.social span{width:14px;height:14px;border-radius:50%;background:var(--white);opacity:.9}
</style>
</head>
<body>

<header class="abs hero">
  <div class="abs brand" style="left:85px;top:22px">KinTrail</div>
  <a class="btn btn-green" style="left:1018px;top:25px;width:97px;height:32px;font-size:13px">Sign in</a>
  <div class="art" role="img" aria-label="Round badge with a family tree emblem and the words Easy to Research, Easy to Share" style="left:230px;top:90px;width:360px;height:380px;background:linear-gradient(180deg,#7cc84e,#4a88c7)"></div>
  <a class="btn btn-green" style="left:674px;top:274px;width:182px;height:55px;font-size:16px">Get started</a>
</header>

<section>
  <h2 class="section-title" style="left:87px;top:640px">Easy to Research</h2>
  <ul class="checks" style="left:87px;top:700px;width:690px">
    <li>Get hints from LineageHub, RecordNook, and other partners... you don't even need to sync your tree with LineageHub to get hints.</li>
    <li>KinTrail Web Clipper automatically copies data from major genealogy websites into your tree. It's 60% faster and more accurate.</li>
    <li>Evidence analysis report and timeline details help you easily analyze and resolve conflicting information contained in sources</li>
  </ul>
  <a class="btn btn-outline" style="left:87px;top:866px;width:125px;height:45px">Read More &gt;</a>
  <div class="art" role="img" aria-label="Illustration of a hand holding a magnifying glass over an ancestor portrait" style="left:836px;top:594px;width:212px;height:366px;background:linear-gradient(180deg,#eef6ea,#cfe8c1)"></div>
</section>

<section class="abs share">
  <div class="art" role="img" aria-label="Illustration of a hand holding a phone sharing photos with three relatives" style="left:137px;top:23px;width:287px;height:349px;background:linear-gradient(180deg,#6ea3d6,#5b95cf)"></div>
  <h2 class="section-title" style="left:599px;top:80px;color:var(--white)">Easy to Share</h2>
  <ul class="checks" style="left:599px;top:140px;width:590px;color:var(--white)">
    <li>Pinwall-like Media Wall lets family members browse around to find what they like. No subscription required.</li>
    <li>News feed shows the latest research, documents, and photos you've added to your tree.</li>
    <li>Video maker lets you turn your research into fun videos so you can tell family stories with narration and music.</li>
  </ul>
  <a class="btn btn-green" style="left:599px;top:302px;width:130px;height:45px;font-size:14px;text-transform:none;font-weight:400">Read More &gt;</a>
</section>

<section>
  <h2 class="section-title" style="left:97px;top:1500px;font-size:25px">Integrate with LineageHub...<br>but control your own tree</h2>
  <ul class="checks" style="left:97px;top:1600px;width:580px">
    <li>Sync your tree, documents, and memories with LineageHub but you control your tree. No one can change it without your permission.</li>
    <li>Download your tree (with images!) directly from LineageHub. Keep what you want. Delete what you want. It's your own private copy of your LineageHub tree.</li>
  </ul>
  <a class="btn btn-outline" style="left:97px;top:1736px;width:130px;height:45px">Read More &gt;</a>
  <div class="art" role="img" aria-label="Illustration of a family tree with round member portraits under an Our Family banner" style="left:769px;top:1485px;width:320px;height:324px;background:linear-gradient(180deg,#fbe3c8,#d6dccb)"></div>
</section>

<section class="abs video" role="img" aria-label="Video still of old family photographs pinned on a board">
  <div class="abs brand" style="left:0;width:1200px;top:150px;text-align:center;font-size:96px;opacity:.85">KinTrail</div>
  <svg class="abs" style="left:559px;top:172px" width="80" height="90" viewBox="0 0 80 90"><polygon points="0,0 80,45 0,90" fill="#fff"/></svg>
</section>

<section class="abs demo">
  <div class="abs" style="left:0;top:332px;width:1200px;height:113px;background:var(--sand);border-top:3px solid #333"></div>
  <div class="art" role="img" aria-label="Illustration of a leafy tree hung with framed family photos" style="left:50px;top:70px;width:362px;height:330px;background:linear-gradient(180deg,#8fc862,#6fae3e 70%,#8a6040)"></div>
  <h2 class="section-title" style="left:429px;top:130px;font-size:22px">Demo Trees</h2>
  <a class="btn btn-green" style="left:429px;top:197px;width:277px;height:78px;font-size:20px;font-weight:900">Henry Castwell</a>
  <a class="btn" style="left:731px;top:197px;width:250px;height:78px;font-size:20px;font-weight:900;background:var(--white);border:2px solid #ccc;color:var(--ink)">Arthur Bellwood</a>
</section>

<section>
  <h2 class="section-title" style="left:0;width:1200px;top:2782px;text-align:center;font-size:23px">KinTrail Annual Plans</h2>

  <div class="plan" style="left:87px">
    <div class="plan-name">Free Forever</div><div class="plan-rule"></div>
    <div class="plan-price">FREE</div><div class="plan-rule"></div>
    <ul class="plan-features">
      <li>Invite people to your tree</li><li>Share on social media</li><li>Unlimited video creation</li>
      <li>KinTrail Web Clipper browser extension</li><li class="off">Turn off ads</li><li class="off">Trees can be marked private*</li>
      <li>2 Family Trees</li><li>1 GB Storage</li>
    </ul>
    <div class="plan-btn">Get started</div>
  </div>

  <div class="plan plan-featured" style="left:439px">
    <svg class="abs" style="left:0;top:0" width="70" height="70" viewBox="0 0 70 70"><polygon points="0,0 70,0 0,70" fill="#f4c21b"/></svg>
    <div class="plan-name" style="margin-top:51px">Standard</div><div class="plan-rule"></div>
    <div class="plan-price">$19.95/YR</div><div class="plan-rule"></div>
    <ul class="plan-features">
      <li>Invite people to your tree</li><li>Share on social media</li><li>Unlimited video creation</li>
      <li>KinTrail Web Clipper browser extension</li><li>Turn off ads</li><li class="off">Trees can be marked private*</li>
      <li>4 Family Trees</li><li>2 GB Storage</li>
    </ul>
    <div class="plan-btn">Get started</div>
  </div>

  <div class="plan" style="left:788px">
    <div class="plan-name">Pro</div><div class="plan-rule"></div>
    <div class="plan-price">$34.95/YR</div><div class="plan-rule"></div>
    <ul class="plan-features">
      <li>Invite people to your tree</li><li>Share on social media</li><li>Unlimited video creation</li>
      <li>KinTrail Web Clipper browser extension</li><li>Turn off ads</li><li>Trees can be marked private*</li>
      <li>10 Family Trees</li><li>10 GB Storage</li>
    </ul>
    <div class="plan-btn">Get started</div>
  </div>

  <p class="abs" style="left:0;width:1200px;top:3440px;text-align:center;font-size:12px;color:var(--muted)">* No matter which plan you choose, information about living people is always kept private</p>
</section>

<footer class="abs footer">
  <div class="foot-head" style="left:87px;top:55px">Quick Links</div>
  <ul class="foot-links" style="left:87px;top:85px">
    <li>&gt; Blog</li><li>&gt; Roadmap</li><li>&gt; Privacy policy</li><li>&gt; Terms of use</li>
  </ul>
  <div class="abs brand" style="left:0;width:1200px;top:80px;text-align:center;font-size:30px">KinTrail</div>
  <div class="abs" style="left:0;width:1200px;top:147px;text-align:center;font-size:12px">Copyright © 2017 KinTrail All rights reserved.</div>
  <div class="foot-head" style="left:948px;top:55px">Follow Us</div>
  <div class="social" style="left:950px;top:92px"><span></span><span></span><span></span><span></span><span></span></div>
</footer>

</body>
</html>
```